Communication Business Card Design

We offer complete cabling solutions
Data Cabling,Fibre Optic, and Cabling Repairs fault finding
Security camera installation
TV Aerial installation
Security alarm installation
QWV

Industry/Entity Type

Business

Contact Information for Business Card

Threadmore Solutions
ABN 52 918 374 260
EMAIL threadmoresolutions.com.au
Mobile 0418362057
Rob Kesler

```html
<!DOCTYPE html>
<html lang="en">
<head>
<meta charset="utf-8">
<title>Threadmore Solutions – Business Card</title>
<link href="https://fonts.googleapis.com/css2?family=Tinos&family=Open+Sans:wght@400&display=swap" rel="stylesheet">
<style>
  :root {
    --page-bg: #d9d9d9;
    --brand-blue: #3a48a6;
    --ink: #111111;
    --white: #ffffff;
    --navy-deep: #05091c;
    --navy-mid: #101c4a;
    --band-1: #1e3f9a;
    --band-2: #2f5bbf;
    --band-3: #4a78d2;
    --photo-dark: #0b2350;
    --photo-light: #3f7fc8;
    --icon-blue: #2c3f9e;
  }
  * { margin: 0; padding: 0; box-sizing: border-box; }
  html, body { width: 992px; height: 1200px; overflow: hidden; }
  body { background: var(--page-bg); position: relative; font-family: "Tinos", "Times New Roman", serif; }

  .card {
    position: absolute;
    left: 68px;
    width: 869px;
    height: 494px;
    border-radius: 22px;
    overflow: hidden;
    box-shadow: 0 6px 12px rgba(0,0,0,0.35);
  }
  .card--front { top: 68px; background: var(--white); }
  .card--back { top: 627px; background: linear-gradient(180deg, var(--navy-mid) 0%, var(--navy-deep) 55%, #0a1235 100%); }

  .front-art { position: absolute; inset: 0; width: 100%; height: 100%; }

  .company-name {
    position: absolute;
    right: 40px;
    font-weight: 400;
    letter-spacing: 1px;
    white-space: nowrap;
  }
  .card--front .company-name { top: 20px; font-size: 46px; color: var(--brand-blue); }

  .person-name {
    position: absolute; right: 42px; top: 136px;
    font-size: 36px; color: var(--ink);
  }
  .contact-list { position: absolute; right: 42px; top: 246px; text-align: right; }
  .contact-line {
    display: flex; justify-content: flex-end; align-items: center;
    font-size: 21px; color: var(--ink); height: 36px;
  }
  .contact-icon { width: 14px; height: 14px; margin-left: 14px; }
  .contact-line--abn { margin-right: 0; font-size: 19px; letter-spacing: 0.5px; }

  .cable-visual {
    position: absolute; left: 0; top: 0; width: 100%; height: 400px;
    background:
      radial-gradient(ellipse 45% 35% at 62% 62%, rgba(80,150,255,0.55), rgba(80,150,255,0) 70%),
      radial-gradient(ellipse 22% 55% at 22% 45%, rgba(40,40,50,0.9), rgba(20,20,30,0) 80%),
      linear-gradient(180deg, var(--navy-mid) 0%, #07103a 100%);
  }
  .card--back .company-name {
    left: 0; right: 0; top: 28px; text-align: center;
    font-size: 46px; color: var(--white); padding-left: 20px;
  }
  .service-list {
    position: absolute; left: 0; right: 0; top: 404px;
    font-family: "Open Sans", Arial, sans-serif; font-size: 19px; color: var(--white);
    text-align: center;
  }
  .service-row { height: 36px; line-height: 36px; white-space: nowrap; }
  .service-row span::before { content: "\2022"; margin-right: 5px; }
  .service-row span + span { margin-left: 10px; }
</style>
</head>
<body>

<section class="card card--front">
  <svg class="front-art" viewBox="0 0 869 494" aria-hidden="false">
    <defs>
      <linearGradient id="photoTone" x1="0" y1="0" x2="1" y2="1">
        <stop offset="0" stop-color="#0d2a5e"/>
        <stop offset="0.5" stop-color="#2a66b4"/>
        <stop offset="1" stop-color="#0b2350"/>
      </linearGradient>
    </defs>
    <rect class="network-photo" x="0" y="0" width="869" height="494" fill="url(#photoTone)" role="img" aria-label="Network cables with RJ45 connectors over a blue digital background"/>
    <path class="wave-band wave-band--outer" fill="#163a8e" d="M0,0 L70,0 C150,70 190,270 360,400 C500,490 720,470 869,380 L869,494 L0,494 Z" opacity="0"/>
    <path class="wave-band wave-band--deep" fill="var(--band-1)" d="M56,0 C140,70 190,280 360,395 C500,480 720,450 869,370 L869,330 C700,420 500,440 400,390 C250,300 170,80 100,0 Z"/>
    <path class="wave-band wave-band--mid" fill="var(--band-2)" d="M70,0 C150,70 200,280 370,385 C510,460 720,430 869,355 L869,330 C700,410 510,430 400,380 C250,290 170,80 100,0 Z"/>
    <path class="wave-band wave-band--light" fill="var(--band-3)" d="M84,0 C160,70 210,280 380,375 C520,445 720,415 869,345 L869,330 C700,400 520,420 400,372 C260,290 180,80 110,0 Z"/>
    <path class="white-field" fill="var(--white)" d="M40,0 L869,0 L869,330 C700,400 520,415 400,368 C260,290 180,100 100,30 C80,15 60,5 40,0 Z"/>
  </svg>

  <h1 class="company-name">THREADMORE SOLUTIONS</h1>
  <p class="person-name">Rob Kesler</p>
  <div class="contact-list">
    <p class="contact-line">0418362057
      <svg class="contact-icon" viewBox="0 0 14 14"><rect width="14" height="14" fill="var(--icon-blue)"/><path d="M4 3 L6 3 L6.5 5.5 L5.5 6.3 C6 7.5 6.8 8.3 8 8.8 L8.8 7.8 L11 8.3 L11 10.3 C7 10.5 3.6 7.2 4 3 Z" fill="#fff"/></svg>
    </p>
    <p class="contact-line">threadmoresolutions.com.au
      <svg class="contact-icon" viewBox="0 0 14 14"><rect width="14" height="14" fill="var(--icon-blue)"/><rect x="3" y="4.5" width="8" height="5.5" fill="#fff"/><path d="M3 4.5 L7 7.8 L11 4.5" fill="none" stroke="var(--icon-blue)" stroke-width="0.9"/></svg>
    </p>
    <p class="contact-line contact-line--abn">ABN 52 918 374 260</p>
  </div>
</section>

<section class="card card--back">
  <div class="cable-visual" role="img" aria-label="Fibre optic cable with coloured inner tubes and glowing light strands"></div>
  <h2 class="company-name">THREADMORE SOLUTIONS</h2>
  <div class="service-list">
    <p class="service-row"><span>Security alarm installation</span> <span>TV Aerial installation</span> <span>Security camera installation</span> <span>QWV</span></p>
    <p class="service-row"><span>Data Cabling,Fibre Optic, and Cabling Repairs fault finding</span></p>
  </div>
</section>

</body>
</html>
```